KWT BUSINESS CARD

I'd like a new business card for the folks in my office. I recently became aware of a company that produces extra thick cards that seem to me to make excellent use of embossing. I have a logo that I like so I just need a design that uses embossing effectively, is simple and uses minimal color.

I am uploading our current logo of a tooth with a brush above it. I am also uploading another file with the words of our business. In your design please use the square version of the tooth vs. the strectched version. The original logo is the more square image but please use the words and the fonts of "Wexmoor Dental Group" and incorporate that in the design.

Industry/Entity Type

Business

Colors
ffffff

Requirements
Must have
• Logo, company name (also a part of our existing logo), employee name and title, phone number and website address. Must be simple
Nice to have
• Embossed - Maybe a solid color on the back
Should not have
• Must not be too complex or busy

```html
<!DOCTYPE html>
<html lang="en">
<head>
<meta charset="utf-8">
<title>Wexmoor Dental Group – Business Card</title>
<link rel="stylesheet" href="https://fonts.googleapis.com/css2?family=Crimson+Text:wght@400&family=Montserrat:wght@800&display=swap">
<style>
  :root {
    --bg: #e9e6e1;
    --card: #fbfbfa;
    --blue: #3a47a0;
    --green: #15b04a;
    --ink: #111111;
    --rule: #8a8a8a;
    --text: #222222;
  }
  * { box-sizing: border-box; margin: 0; padding: 0; }
  html, body { width: 1200px; height: 1023px; overflow: hidden; background: var(--bg); }
  .canvas { position: relative; width: 1200px; height: 1023px; }
  .card {
    position: absolute; left: 215px; width: 770px; height: 440px;
    background: var(--card); border-radius: 14px; overflow: hidden;
    box-shadow: 0 6px 18px rgba(0,0,0,.18);
  }
  .card--front { top: 48px; }
  .card--back { top: 535px; }

  .stripe-blue { position: absolute; left: 0; right: 0; height: 7px; background: var(--blue); }
  .stripe-green { position: absolute; left: 0; right: 0; bottom: 0; background: var(--green); }
  .card--front .stripe-blue { top: 392px; }
  .card--front .stripe-green { height: 30px; }
  .card--back .stripe-blue { top: 364px; }
  .card--back .stripe-green { height: 56px; }

  .rule { position: absolute; height: 1px; background: var(--rule); }
  .rule--top { top: 118px; left: 460px; right: 0; }
  .rule--mid { top: 292px; left: 0; right: 0; }

  .brand-mark { position: absolute; display: flex; align-items: center; gap: 14px; }
  .brand-mark__square { background: var(--green); flex: none; }
  .brand-mark__name { font-family: "Montserrat", sans-serif; font-weight: 800; color: var(--blue); line-height: 1.05; }
  .card--front .brand-mark { left: 250px; top: 70px; }
  .card--front .brand-mark__square { width: 40px; height: 40px; }
  .card--front .brand-mark__name { font-size: 22px; }

  .person { position: absolute; left: 370px; top: 238px; text-align: right; width: 240px; }
  .person__name { font-family: "Crimson Text", serif; font-size: 27px; color: var(--blue); letter-spacing: .5px; }
  .person__title { font-family: "Crimson Text", serif; font-size: 17px; color: var(--text); margin-top: -4px; }

  .contact { position: absolute; left: 38px; top: 308px; list-style: none; }
  .contact li { display: flex; align-items: center; gap: 12px; font-family: "Crimson Text", serif; font-size: 19px; color: var(--text); height: 26px; }
  .contact svg { width: 16px; height: 16px; flex: none; }

  .back-square { position: absolute; left: 70px; top: 60px; width: 270px; height: 270px; background: var(--blue); }
  .wordmark {
    position: absolute; left: 380px; top: 95px;
    font-family: "Montserrat", sans-serif; font-weight: 800; color: var(--ink);
    font-size: 62px; line-height: 1.02; letter-spacing: 1px;
  }
  .site {
    position: absolute; right: 40px; bottom: 16px;
    font-family: "Crimson Text", serif; font-size: 19px; color: #ffffff;
  }
</style>
</head>
<body>
<div class="canvas">

  <section class="card card--front">
    <div class="rule rule--top"></div>
    <div class="brand-mark">
      <span class="brand-mark__square"></span>
      <span class="brand-mark__name">Wexmoor<br>Dental Group</span>
    </div>
    <div class="person">
      <p class="person__name">DANA HOLLOWAY</p>
      <p class="person__title">office manager</p>
    </div>
    <div class="rule rule--mid"></div>
    <ul class="contact">
      <li>
        <svg viewBox="0 0 16 16"><path d="M4 1c-1 0-2 1-2 2 0 6 5 11 11 11 1 0 2-1 2-2v-2l-3-1-2 2C8 10 6 8 5 6l2-2-1-3z" fill="var(--green)"/></svg>
        555-014-2290
      </li>
      <li>
        <svg viewBox="0 0 16 16"><rect x="1" y="3" width="14" height="10" fill="none" stroke="var(--green)" stroke-width="1.5"/><path d="M1 3l7 6 7-6" fill="none" stroke="var(--green)" stroke-width="1.5"/></svg>
        danaholloway@email.com
      </li>
      <li>
        <svg viewBox="0 0 16 16"><circle cx="8" cy="8" r="7" fill="var(--green)"/><path d="M1 8h14M8 1c-3 4-3 10 0 14M8 1c3 4 3 10 0 14" fill="none" stroke="#fff" stroke-width="1"/></svg>
        www.wexmoordentalgroup.com
      </li>
    </ul>
    <div class="stripe-blue"></div>
    <div class="stripe-green"></div>
  </section>

  <section class="card card--back">
    <div class="back-square"></div>
    <p class="wordmark">WEXMOOR<br>DENTAL<br>GROUP</p>
    <div class="stripe-blue"></div>
    <div class="stripe-green"><p class="site">www.wexmoordentalgroup.com</p></div>
  </section>

</div>
</body>
</html>
```